Etiketten für Kürbiskernöl
Zielgruppe
Wir betreiben eine Landwirschaft, vorwiegend Ackerbau und Viehwirtschaft im nordöstlichen Niederösterreich. Wir sind ein reines Familienunternehmen. Unsere Zielgruppe ist 20 Jahre aufwärts, männlich wie weiblich und legt großen Wert auf Regionalität und hohe Qualität der Produkte.
Aufgabenstellung
Das Etikett wird für unsere Kürbiskernölflasche benötigt. Die Vorderseite soll unseren Namen, Produktbezeichnung und Füllmenge enthalten. Familie Wendtner - Kürbiskernöl 100% rein - 500ml Für die Rückseite gibt es einen entsprechenden Text (siehe Anhang).
Angehängt haben wir auch Etikett Vorderseiten, die uns sehr ansprechen. Es soll auf jeden Fall ein Kürbis abgebildet sein und ein hochwertiges, eher minimalistischen Design haben.
In Zukunft könnten wir uns auch vorstellen die Kürbiskerne in Form von Knabberkernen zu verkaufen, wofür wir das Etikettendesign gern abwandeln würden.
Farben: dunkelgrau/schwarz, weiß, dunkelgrün/oliv, beige
Flaschenform: Valmera 500ml siehe Foto

```html
<!DOCTYPE html>
<html lang="de">
<head>
<meta charset="utf-8">
<title>Etiketten Kürbiskernöl – Familie Wendtner</title>
<link rel="stylesheet" href="https://fonts.googleapis.com/css2?family=Allura&family=Montserrat:wght@300;400&display=swap">
<style>
  :root {
    --canvas: #ffffff;
    --label: #221f20;
    --ink: #f4f2ee;
    --art-light: #4a4647;
    --art-dark: #2c2829;
  }
  * { margin: 0; padding: 0; box-sizing: border-box; }
  html, body { width: 1200px; height: 600px; overflow: hidden; background: var(--canvas); }
  .sheet { position: relative; width: 1200px; height: 600px; }

  .label {
    position: absolute;
    top: 25px;
    width: 245px;
    height: 550px;
    background: var(--label);
    color: var(--ink);
    font-family: "Montserrat", sans-serif;
    font-weight: 300;
  }
  .label--back { left: 337px; }
  .label--front { left: 618px; }

  .label__block { position: absolute; left: 25px; width: 200px; font-size: 9.4px; line-height: 11.7px; }
  .label__script { position: absolute; font-family: "Allura", cursive; color: var(--ink); }

  .back__intro { top: 27px; }
  .back__claim { top: 80px; left: 47px; font-size: 15px; }
  .back__process { top: 121px; }
  .back__address { top: 268px; }
  .back__storage { top: 308px; font-size: 8.6px; }
  .back__date-row { position: absolute; top: 330px; left: 25px; display: flex; align-items: baseline; gap: 9px; font-size: 8.6px; }
  .back__date { font-family: "Allura", cursive; font-size: 19px; }
  .back__volume { position: absolute; right: 14px; bottom: 11px; font-size: 13px; font-weight: 400; letter-spacing: 0.02em; }

  .front__brand { position: absolute; top: 27px; left: 0; width: 100%; text-align: center; }
  .front__family { font-size: 12.5px; font-weight: 400; letter-spacing: 0.32em; padding-left: 0.32em; }
  .front__name { margin-top: 6px; font-size: 17px; font-weight: 400; letter-spacing: 0.12em; }

  .front__product { position: absolute; top: 188px; left: 40px; font-size: 25px; font-weight: 400; letter-spacing: 0.3em; line-height: 31px; }
  .front__purity { position: absolute; top: 258px; left: 150px; width: 78px; height: 17px; }
  .front__stroke { position: absolute; inset: 0; background: var(--ink); }
  .front__purity-text { position: absolute; inset: 0; text-align: center; font-family: "Allura", cursive; font-size: 14px; line-height: 18px; color: var(--label); }

  .art { position: absolute; border-radius: 46% 46% 38% 38%; }
  .art--back { left: 4px; top: 384px; width: 140px; height: 130px; background: radial-gradient(circle at 50% 40%, var(--art-light), var(--art-dark)); }
  .art--front { left: 8px; top: 384px; width: 231px; height: 144px; background: radial-gradient(ellipse at 45% 45%, var(--art-light), var(--art-dark)); }
</style>
</head>
<body>
<main class="sheet">

  <section class="label label--back" aria-label="Etikett Rückseite">
    <p class="label__block back__intro">Nur die besten Kürbiskerne aus unserem eigenen Anbau werden zu unserem g'sund, g'schmackig, guatem Kürbiskernöl verarbeitet.</p>
    <p class="label__script back__claim">100% rein und naturbelassen</p>
    <p class="label__block back__process">Die Kürbiskerne werden schonend geröstet und in einem traditionellen Verfahren in einer regionalen Ölmühle kalt gepresst, was unserem Kürbiskernöl das einzigartige, intensiv-nussige Aroma verleiht.</p>
    <p class="label__block back__address">Familie Wendtner<br>2071 Lindenau 47</p>
    <p class="label__block back__storage">Vor Wärme und Licht geschützt lagern.</p>
    <p class="back__date-row"><span>Mindestens haltbar bis:</span><span class="back__date">Oktober 2022</span></p>
    <div class="art art--back" role="img" aria-label="Weiße Strichzeichnung eines Kürbisses"></div>
    <p class="back__volume">500 ML</p>
  </section>

  <section class="label label--front" aria-label="Etikett Vorderseite">
    <div class="front__brand">
      <p class="front__family">FAMILIE</p>
      <p class="front__name">WENDTNER</p>
    </div>
    <h1 class="front__product">KÜRBIS<br>KERNÖL</h1>
    <div class="front__purity">
      <span class="front__stroke" role="img" aria-label="Weißer Pinselstrich"></span>
      <span class="front__purity-text">100% rein</span>
    </div>
    <div class="art art--front" role="img" aria-label="Weiße Strichzeichnung eines Kürbisses mit aufgeschnittenem Stück und Kernen"></div>
  </section>

</main>
</body>
</html>
```